Business card Pfotenweide

Business card is for a self-employed dog trainer with own dog school. Name and logo of the dog school are available. Color specifications as well. The design should be classy and minimalist, but also modern. An already existing idea would be: Front: Only the logo Back: Contact data

Font styles to use
Serif
Sans Serif
Other font styles liked:
• Trajan Pro

Colors
f78f20

Requirements
Must have
• Name: Marlene Kessel-Brand Title: Dipl. Dog Trainer Contain my logo Follow my font and color preferences (see files)

```html
<!DOCTYPE html>
<html lang="de">
<head>
<meta charset="utf-8">
<title>Pfotenweide – Visitenkarte</title>
<link rel="stylesheet" href="https://fonts.googleapis.com/css2?family=Cinzel:wght@400;500&family=Lora:wght@400&display=swap">
<style>
  :root {
    --stage: #3b3b3d;
    --card: #232325;
    --card-sheen: #2c2c2f;
    --ink: #f2f0ec;
    --tan: #8a7462;
    --slate: #4f5659;
    --emboss: #1b1b1d;
  }
  * { box-sizing: border-box; margin: 0; padding: 0; }
  html, body { width: 799px; height: 1200px; overflow: hidden; background: var(--stage); }
  .canvas { position: relative; width: 799px; height: 1200px; }
  .card {
    position: absolute; left: 90px; width: 620px; height: 354px;
    background: linear-gradient(135deg, var(--card-sheen), var(--card));
    box-shadow: 0 18px 40px rgba(0,0,0,.45);
    overflow: hidden;
  }
  .card--front { top: 150px; }
  .card--back { top: 690px; }

  .front-mark {
    position: absolute; left: 50%; top: 50%; width: 230px; height: 230px;
    transform: translate(-50%, -50%); border-radius: 50%;
    background: radial-gradient(circle at 40% 35%, #3a3a3d, var(--emboss));
    border: 2px solid #46464a;
    display: flex; align-items: center; justify-content: center;
  }
  .front-mark__name {
    font-family: "Cinzel", serif; font-weight: 400; font-size: 24px;
    letter-spacing: 2px; color: #5a5a5e;
  }

  .brand { position: absolute; left: 30px; top: 34px; display: flex; align-items: center; gap: 12px; }
  .brand__dot { width: 62px; height: 62px; border-radius: 50%; background: var(--tan); }
  .brand__name {
    font-family: "Cinzel", serif; font-weight: 400; font-size: 38px;
    letter-spacing: 1px; color: var(--ink);
  }

  .person { position: absolute; left: 40px; top: 140px; color: var(--ink); }
  .person__name { font-family: "Cinzel", serif; font-size: 18px; font-weight: 400; letter-spacing: .5px; }
  .person__title { font-family: "Lora", serif; font-size: 10px; margin-top: 6px; }

  .contact { position: absolute; left: 330px; top: 192px; list-style: none; color: var(--ink); }
  .contact li {
    display: flex; align-items: center; gap: 10px;
    font-family: "Lora", serif; font-size: 16px; line-height: 24px;
  }
  .contact svg { width: 12px; height: 12px; fill: var(--tan); flex: none; }

  .bands { position: absolute; left: 0; top: 0; }
  .web {
    position: absolute; left: 360px; top: 312px; width: 240px; text-align: center;
    font-family: "Lora", serif; font-size: 17px; color: var(--ink);
  }
</style>
</head>
<body>
<main class="canvas">

  <section class="card card--front" aria-label="Vorderseite">
    <div class="front-mark">
      <span class="front-mark__name">PFOTENWEIDE</span>
    </div>
  </section>

  <section class="card card--back" aria-label="Rückseite">
    <svg class="bands" width="620" height="354" viewBox="0 0 620 354" aria-hidden="true">
      <polygon points="0,306 336,306 310,354 0,354" fill="var(--slate)"/>
      <polygon points="350,280 620,280 620,354 310,354" fill="var(--tan)"/>
    </svg>

    <div class="brand">
      <span class="brand__dot"></span>
      <span class="brand__name">PFOTENWEIDE</span>
    </div>

    <div class="person">
      <p class="person__name">MARLENE KESSEL-BRAND</p>
      <p class="person__title">Dipl. Dog Trainer</p>
    </div>

    <ul class="contact">
      <li>
        <svg viewBox="0 0 24 24"><path d="M6.6 10.8a15 15 0 0 0 6.6 6.6l2.2-2.2c.3-.3.7-.4 1-.2 1.1.4 2.3.6 3.6.6.6 0 1 .4 1 1V20c0 .6-.4 1-1 1A17 17 0 0 1 3 4c0-.6.4-1 1-1h3.5c.6 0 1 .4 1 1 0 1.2.2 2.4.6 3.6.1.3 0 .7-.2 1z"/></svg>
        (123) 456-7890
      </li>
      <li>
        <svg viewBox="0 0 24 24"><path d="M2 5h20v14H2zm2 2v.5l8 5 8-5V7z"/></svg>
        marlene@pfotenweide.ch
      </li>
      <li>
        <svg viewBox="0 0 24 24"><path d="M12 2a7 7 0 0 0-7 7c0 5.2 7 13 7 13s7-7.8 7-13a7 7 0 0 0-7-7zm0 9.5A2.5 2.5 0 1 1 12 6.5a2.5 2.5 0 0 1 0 5z"/></svg>
        Lindenweg 12, Bülach
      </li>
    </ul>

    <p class="web">www.pfotenweide.ch</p>
  </section>

</main>
</body>
</html>
```